Scandinavian Online Sewing store need a flier

We need a 'flier' or over sized business card to include with orders which are shipped to customers. We are based in Norway and looking for something which will appeal to the Scandinavian market. The business name is 'Tråkroken' which in English means 'sewing cupboard'.

We are aiming for the younger market sector and stocking 'fresher' and 'younger' fabric, patterns and notions. (See Stitch by day, Walden+T, Harbour & Pike, Valdrine K etc.)

We would like a A5/A6 sized card which we could use in place of a business card. It should include the logo and perhaps a textured background (either paper or fabric).

Looking forward to see the ideas of all you amazingly creative souls!

Target Market(s)

Scandinavian home sewers who are interested in creating and design

Industry/Entity Type

Textile

Requirements
Must have
• logo (Attached to project) picture or artwork
Nice to have
• texture background

```html
<!DOCTYPE html>
<html lang="no">
<head>
<meta charset="utf-8">
<title>Tråkroken – flier</title>
<link rel="stylesheet" href="https://fonts.googleapis.com/css2?family=Amatic+SC:wght@700&family=Ubuntu:wght@300;400&display=swap">
<style>
  :root {
    --cloth-light: #8b7f73;
    --cloth-mid: #675c53;
    --cloth-dark: #2f2925;
    --stitch: #35312d;
    --card-green: #a8b98f;
    --card-edge: #2b2b28;
    --art-dark: #2a2a27;
    --art-mid: #7f8e6c;
    --ink: #141414;
    --white: #f6f3ee;
    --tagline: #c9c2b8;
    --url-green: #b3c595;
  }
  * { margin: 0; padding: 0; box-sizing: border-box; }
  html, body { width: 849px; height: 1200px; overflow: hidden; }
  body { background: var(--cloth-dark); }

  .flier {
    position: relative;
    width: 849px;
    height: 1200px;
    overflow: hidden;
    background:
      radial-gradient(ellipse 70% 45% at 50% 28%, rgba(255,255,255,0.08), transparent 70%),
      linear-gradient(180deg, var(--cloth-light) 0%, var(--cloth-mid) 45%, var(--cloth-dark) 100%);
  }

  .stitch-frame {
    position: absolute;
    left: 226px;
    top: 104px;
    width: 402px;
    height: 520px;
  }

  .label-card {
    position: absolute;
    left: 250px;
    top: 124px;
    width: 354px;
    height: 484px;
    background: var(--card-green);
    border: 4px solid var(--card-edge);
    box-shadow: 0 6px 14px rgba(0,0,0,0.35);
  }
  .brand-name {
    position: absolute;
    top: 4px;
    left: 0;
    width: 100%;
    text-align: center;
    font-family: "Amatic SC", cursive;
    font-weight: 700;
    font-size: 86px;
    line-height: 1;
    letter-spacing: 2px;
    color: var(--ink);
  }
  .notions-art {
    position: absolute;
    left: 20px;
    top: 96px;
    width: 306px;
    height: 366px;
    background: linear-gradient(160deg, var(--art-mid), var(--art-dark) 140%);
  }

  .headline {
    position: absolute;
    top: 642px;
    left: 0;
    width: 100%;
    text-align: center;
    font-family: "Amatic SC", cursive;
    font-weight: 700;
    font-size: 92px;
    line-height: 112px;
    color: var(--white);
    letter-spacing: 1px;
  }
  .tagline {
    position: absolute;
    top: 866px;
    left: 0;
    width: 100%;
    text-align: center;
    font-family: "Ubuntu", sans-serif;
    font-weight: 300;
    font-size: 15px;
    letter-spacing: 0.5px;
    color: var(--tagline);
  }
  .web-address {
    position: absolute;
    top: 1004px;
    left: 0;
    width: 100%;
    text-align: center;
    font-family: "Ubuntu", sans-serif;
    font-weight: 400;
    font-size: 56px;
    color: var(--url-green);
  }
</style>
</head>
<body>
  <main class="flier">
    <svg class="stitch-frame" viewBox="0 0 402 520" aria-hidden="true">
      <rect x="4" y="4" width="394" height="512" fill="none" stroke="var(--stitch)" stroke-width="7" stroke-dasharray="22 10"/>
    </svg>

    <section class="label-card">
      <div class="brand-name">Tråkroken</div>
      <div class="notions-art" role="img" aria-label="Illustration of sewing notions: thread spools, measuring tape, scissors, pincushion, buttons and ribbons"></div>
    </section>

    <h1 class="headline">Fristelser for de som<br>elsker å skaper</h1>
    <p class="tagline">TEMPTATIONS FOR THOSE WHO LOVE TO CREATE</p>
    <p class="web-address">www.trakroken.no</p>
  </main>
</body>
</html>
```